Wedding Vow Design for Modern Print - SUBWAY PRINT STYLE or Similar, MODERN

I recently got married and I want to take the main words from my wedding vows and create a design using them that I can have printed and present to my new wife. I told her that I had privileges with Marring her and I made her promises. I would like to highlight both. We have a modern home and I want something that we can have professionally framed and hung on the wall. Love modern and clean design but something interesting.

Target Market(s)

Myself. 35, modern and loves clean design.

Industry/Entity Type

Wedding

Font styles to use
Serif

Colors
f6f3f8
ffffff
fbd4d5
000000
9d9d9d
dddddd

Requirements
Must have
• Cool, clean and modern design. Neutral Colors, Clean lines, Black and White, no reds, pinks, etc.
• We will hang this in our California modern home.
Nice to have
• Our wedding colors were , Gray,Black, Light Pink. I love the Subway signs and also love Black and White Word art.
Should not have
• Flowers, squiggly lines, traditional design. Something that would look great in a stainless metal frame or mirrored frame on white walls.

```html
<!DOCTYPE html>
<html lang="en">
<head>
<meta charset="utf-8">
<title>Vows — Privileges &amp; Promises</title>
<link rel="stylesheet" href="https://fonts.googleapis.com/css2?family=Questrial&family=Archivo+Narrow:wght@400&display=swap">
<style>
  :root {
    --ink: #000000;
    --paper: #ffffff;
  }
  html, body {
    margin: 0;
    padding: 0;
    width: 848px;
    height: 1200px;
    overflow: hidden;
    background: var(--ink);
  }
  .vow-poster {
    display: block;
    width: 848px;
    height: 1200px;
    background: var(--ink);
  }
  .word {
    fill: var(--paper);
    font-family: "Questrial", "Century Gothic", sans-serif;
  }
  .word--narrow {
    font-family: "Archivo Narrow", "Arial Narrow", sans-serif;
  }
</style>
</head>
<body>
<svg class="vow-poster" viewBox="0 0 848 1200" xmlns="http://www.w3.org/2000/svg" role="img" aria-label="Wedding vow word art: privileges and promises">
  <rect class="backdrop" width="848" height="1200" fill="var(--ink)"/>

  <g class="row row--privileges">
    <text class="word" x="18" y="98" font-size="96" textLength="548" lengthAdjust="spacingAndGlyphs">PRIVILEGES</text>
    <text class="word" x="572" y="61" font-size="43" textLength="250" lengthAdjust="spacingAndGlyphs">REST OF</text>
    <text class="word" x="572" y="107" font-size="43" textLength="250" lengthAdjust="spacingAndGlyphs">MY LIFE</text>
  </g>

  <g class="row row--care">
    <text class="word" x="18" y="194" font-size="39" textLength="264" lengthAdjust="spacingAndGlyphs">PROVISION</text>
    <text class="word" x="331" y="194" font-size="39" textLength="212" lengthAdjust="spacingAndGlyphs">PURPOSE</text>
    <text class="word" x="18" y="251" font-size="39" textLength="298" lengthAdjust="spacingAndGlyphs">PROTECTION</text>
    <text class="word" x="333" y="251" font-size="39" textLength="217" lengthAdjust="spacingAndGlyphs">PATIENCE</text>
    <text class="word" x="565" y="250" font-size="122" textLength="257" lengthAdjust="spacingAndGlyphs">CARE</text>
  </g>

  <g class="row row--love">
    <text class="word" x="18" y="371" font-size="83" textLength="804" lengthAdjust="spacingAndGlyphs">LOVE – REGARDLESS</text>
  </g>

  <g class="row row--provision">
    <text class="word" x="18" y="561" font-size="162" textLength="804" lengthAdjust="spacingAndGlyphs">PROVISION</text>
  </g>

  <g class="row row--promises">
    <text class="word" x="18" y="711" font-size="101" textLength="530" lengthAdjust="spacingAndGlyphs">PROMISES</text>
    <text class="word" x="568" y="672" font-size="49" textLength="68" lengthAdjust="spacingAndGlyphs">BY</text>
    <text class="word" x="668" y="672" font-size="49" textLength="154" lengthAdjust="spacingAndGlyphs">YOUR</text>
    <text class="word" x="666" y="719" font-size="49" textLength="87" lengthAdjust="spacingAndGlyphs">SIDE</text>
  </g>

  <g class="row row--support">
    <text class="word word--narrow" x="18" y="820" font-size="50" textLength="530" lengthAdjust="spacingAndGlyphs">UNCONDITIONAL SUPPORT</text>
    <text class="word word--narrow" x="62" y="862" font-size="50" textLength="440" lengthAdjust="spacingAndGlyphs">FIGHT SAFETY CHERISH</text>
    <text class="word word--narrow" x="567" y="860" font-size="102" textLength="255" lengthAdjust="spacingAndGlyphs">Listen</text>
  </g>

  <g class="row row--best">
    <text class="word" x="18" y="1009" font-size="119" textLength="804" lengthAdjust="spacingAndGlyphs">THE BEST IN YOU</text>
    <text class="word" x="18" y="1136" font-size="119" textLength="804" lengthAdjust="spacingAndGlyphs">THE BEST IN ME</text>
  </g>
</svg>
</body>
</html>
```